Talvor Visit cards serious but not sad

Hello, I'd like to design my visit cards with the logo Talvor (attached) the following information: Name: Karim Belmadi Title: Mobile Director: 33 (0) 6 72 18 35 09 Phone: 33 (0) 4 58 61 07 92 e-mail: karim.belmadi@talvor-consulting.example address: 17 Rue Marcel Danvin 92730 Versanne This visit will be used on the banking institutions and Talvor is a consulting firm. I do not want to have dark background.

Target Market(s)

banks

Contact Information for Business Card

Name : Karim Belmadi
Title : Director
mobile : +33(0)6 72 18 35 09
Phone : +33(0)4 58 61 07 92
e-mail: karim.belmadi@talvor-consulting.example
adresse : 17 Rue marcel Danvin 92400 Courbevoie

Requirements
Nice to have
• serious but not sad

```html
<!DOCTYPE html>
<html lang="en">
<head>
<meta charset="utf-8">
<title>Talvor – Business Card</title>
<link rel="stylesheet" href="https://fonts.googleapis.com/css2?family=Exo+2:wght@400;700;800&family=Open+Sans:wght@300;400&display=swap">
<style>
  :root {
    --brand-blue: #1f6fbf;
    --ink-grey: #4a4d52;
    --soft-grey: #9a9da2;
    --card-white: #ffffff;
    --backdrop: #e8e9eb;
  }
  html, body {
    margin: 0;
    padding: 0;
    width: 1200px;
    height: 1000px;
    overflow: hidden;
    background: var(--backdrop);
  }
  .canvas {
    position: relative;
    width: 1200px;
    height: 1000px;
  }
  .business-card {
    position: absolute;
    left: 335px;
    top: 90px;
    width: 530px;
    height: 820px;
    background: var(--card-white);
    box-shadow: 0 2px 10px rgba(0,0,0,0.08);
  }
  .brand {
    position: absolute;
    left: 112px;
    top: 62px;
    display: flex;
    align-items: center;
    gap: 18px;
  }
  .brand-dot {
    width: 92px;
    height: 92px;
    border-radius: 50%;
    background: var(--brand-blue);
  }
  .brand-name {
    font-family: "Exo 2", sans-serif;
    font-weight: 700;
    font-size: 76px;
    line-height: 1;
    color: var(--brand-blue);
    letter-spacing: 1px;
  }
  .details {
    position: absolute;
    left: 492px;
    top: 200px;
    width: 520px;
    transform: rotate(90deg);
    transform-origin: top left;
  }
  .person-name {
    margin: 0;
    font-family: "Exo 2", sans-serif;
    font-weight: 800;
    font-size: 31px;
    line-height: 40px;
    color: var(--brand-blue);
    text-transform: uppercase;
    letter-spacing: 0.5px;
    white-space: nowrap;
  }
  .person-title {
    margin: 0;
    font-family: "Open Sans", sans-serif;
    font-weight: 300;
    font-size: 24px;
    line-height: 32px;
    color: var(--soft-grey);
  }
  .contact-list {
    list-style: none;
    margin: 46px 0 0;
    padding: 0;
  }
  .contact-item {
    display: flex;
    align-items: center;
    gap: 14px;
    height: 44px;
    font-family: "Open Sans", sans-serif;
    font-weight: 400;
    font-size: 17px;
    color: var(--ink-grey);
    white-space: nowrap;
  }
  .contact-icon {
    width: 16px;
    height: 16px;
    flex: none;
    fill: none;
    stroke: var(--brand-blue);
    stroke-width: 2;
  }
  .contact-icon .solid { fill: var(--brand-blue); stroke: none; }
</style>
</head>
<body>
<main class="canvas">
  <section class="business-card" aria-label="Talvor business card">
    <div class="brand">
      <span class="brand-dot"></span>
      <span class="brand-name">Talvor</span>
    </div>

    <div class="details">
      <h1 class="person-name">Karim Belmadi</h1>
      <p class="person-title">Director</p>
      <ul class="contact-list">
        <li class="contact-item">
          <svg class="contact-icon" viewBox="0 0 16 16" aria-label="Mobile"><rect x="2" y="2" width="12" height="12" rx="1"/></svg>
          <span>+33 (0) 6 72 18 35 09</span>
        </li>
        <li class="contact-item">
          <svg class="contact-icon" viewBox="0 0 16 16" aria-label="Phone"><path class="solid" d="M3 1.5h3l1.2 3.5-1.8 1.2a8 8 0 0 0 4.4 4.4l1.2-1.8 3.5 1.2v3a1.5 1.5 0 0 1-1.5 1.5A12.5 12.5 0 0 1 1.5 3 1.5 1.5 0 0 1 3 1.5z"/></svg>
          <span>+33 (0) 4 58 61 07 92</span>
        </li>
        <li class="contact-item">
          <svg class="contact-icon" viewBox="0 0 16 16" aria-label="E-mail"><circle cx="8" cy="8" r="2.8"/><path d="M10.8 5.5v3.3a1.8 1.8 0 0 0 3.6 0V8a6.4 6.4 0 1 0-2.6 5.1"/></svg>
          <span>karim.belmadi@talvor-consulting.example</span>
        </li>
        <li class="contact-item">
          <svg class="contact-icon" viewBox="0 0 16 16" aria-label="Address"><path class="solid" d="M8 1a5 5 0 0 0-5 5c0 3.8 5 9 5 9s5-5.2 5-9a5 5 0 0 0-5-5zm0 7a2 2 0 1 1 0-4 2 2 0 0 1 0 4z"/></svg>
          <span>17 Rue Marcel Danvin 92730 Versanne</span>
        </li>
      </ul>
    </div>
  </section>
</main>
</body>
</html>
```